Flyer für Sicherheitsfirma
Zielgruppe
Wir sind eine Sicherheitsfirma und verkaufen und installieren Alarmanlagen, Kamerasysteme und Brandmeldeanlagen.
Aufgabenstellung
Es sollte ein sehr ansprechender Flyer sein, welcher in dem Bewohner des Hauses die Angst weckt das ihm Einbruch oder Brand auch jederzeit widerfahren kann.

```html
<!DOCTYPE html>
<html lang="de">
<head>
<meta charset="utf-8">
<title>Wachkern Sicherheitstechnik – Flyer</title>
<link href="https://fonts.googleapis.com/css2?family=Poppins:wght@400;500;600;700;800&display=swap" rel="stylesheet">
<style>
  :root{
    --green:#8cc63f;
    --green-dark:#6fa82a;
    --dark:#1f1f21;
    --grey:#6d6e70;
    --grey-mid:#77787a;
    --ink:#1a1a1a;
    --white:#ffffff;
    --stage:#e6e6e6;
  }
  *{box-sizing:border-box;margin:0;padding:0}
  html,body{width:1200px;height:1117px;overflow:hidden;background:var(--stage);font-family:"Poppins",sans-serif;color:var(--ink)}
  .canvas{position:relative;width:1200px;height:1117px}
  .page{position:absolute;top:160px;width:560px;height:792px;background:var(--white);overflow:hidden;box-shadow:0 8px 24px rgba(0,0,0,.18)}
  .page--front{left:30px}
  .page--back{left:610px}
  .abs{position:absolute}

  /* front */
  .hero{left:0;top:0;width:560px;height:400px;background:linear-gradient(135deg,#3a3a3c,#161617 60%,#2a2a2c)}
  .top-rule{left:0;top:16px;width:560px;height:6px;background:var(--green)}
  .logo-tab{left:120px;top:14px;width:320px;height:88px}
  .brand{left:120px;top:36px;width:320px;display:flex;align-items:center;justify-content:center;gap:10px;font-weight:600;font-size:30px;color:var(--grey);letter-spacing:.5px}
  .brand__dot{width:30px;height:30px;border-radius:50%;background:var(--green)}
  .brand-sub{left:120px;top:74px;width:320px;text-align:center;font-size:10px;letter-spacing:4px;color:var(--grey);font-weight:500}
  .headline{left:0;top:112px;width:560px;text-align:center;font-weight:800;line-height:1.1}
  .headline__white{display:block;color:var(--white);font-size:31px}
  .headline__green{display:block;color:var(--green);font-size:31px}
  .tagline{left:0;top:196px;width:560px;text-align:center;color:var(--white);font-weight:600;font-size:17px}
  .tagline b{color:var(--green)}
  .thumbs{left:42px;top:230px;width:476px;height:104px;background:var(--white);padding:4px;display:flex;gap:4px}
  .thumb{flex:1}
  .thumb--touch{background:linear-gradient(135deg,#d9dde3,#6f7f95)}
  .thumb--cam{background:linear-gradient(135deg,#e4e1dc,#9a948d 55%,#b9a48a)}
  .thumb--phone{background:linear-gradient(135deg,#6fa7d6,#1f4e7a)}
  .question{left:58px;top:318px;width:230px;height:36px;background:var(--green);color:var(--white);font-weight:700;font-size:16px;display:flex;align-items:center;padding-left:16px}
  .intro{left:66px;top:354px;width:494px;height:76px;background:var(--grey);color:var(--white);font-weight:500;font-size:13px;line-height:1.4;padding:10px 26px}
  .guard-photo{left:10px;top:440px;width:258px;height:300px;background:linear-gradient(160deg,#a7b39a 0%,#5f6b5a 40%,#1c2433 70%,#121826)}
  .offer{left:288px;top:444px;width:250px}
  .offer__title{font-weight:700;font-size:15px;line-height:1.25;padding-bottom:10px;border-bottom:2px solid var(--green)}
  .offer__item{display:flex;gap:12px;padding:12px 0;border-bottom:2px solid var(--green)}
  .offer__item:last-child{border-bottom:none}
  .tick{flex:0 0 38px;height:38px;border-radius:50%;border:3px solid var(--green);background:var(--white);display:flex;align-items:center;justify-content:center}
  .tick span{width:26px;height:26px;border-radius:50%;background:var(--green);display:flex;align-items:center;justify-content:center}
  .offer__name{color:var(--green);font-weight:700;font-size:15px}
  .offer__text{font-size:14px;line-height:1.3}
  .front-footer{left:0;top:740px;width:560px;height:52px;background:var(--green);color:var(--white);font-weight:700;font-size:16px;display:flex;align-items:center;justify-content:center}

  /* back */
  .fleet-photo{left:0;top:0;width:560px;height:190px;background:linear-gradient(180deg,#5f7f4e 0%,#e9eef0 30%,#ffffff 60%,#8d8d8d 100%)}
  .brand--small{left:330px;top:148px;width:220px;font-size:16px;color:var(--white);gap:6px;justify-content:flex-end}
  .brand--small .brand__dot{width:18px;height:18px}
  .brand-sub--small{left:330px;top:168px;width:220px;text-align:right;font-size:6px;letter-spacing:2px;color:var(--white)}
  .why-tag{left:10px;top:176px;width:270px;height:34px;background:var(--green);color:var(--white);font-weight:700;font-size:14px;display:flex;align-items:center;padding-left:22px}
  .dark-band{left:0;top:210px;width:560px;height:220px;background:var(--dark)}
  .benefits{left:26px;top:210px;width:508px;height:236px;background:var(--white);padding:8px 24px}
  .benefit{display:flex;gap:16px;align-items:center;padding:8px 0;border-bottom:1.5px solid var(--green)}
  .benefit:last-child{border-bottom:none}
  .ring{flex:0 0 58px;height:58px;border-radius:50%;border:4px solid var(--green);display:flex;align-items:center;justify-content:center}
  .ring span{width:44px;height:44px;border-radius:50%;background:var(--grey);display:flex;align-items:center;justify-content:center}
  .benefit__title{font-weight:700;font-size:13px}
  .benefit__text{font-size:10px;line-height:1.4}
  .bags-photo{left:26px;top:446px;width:234px;height:254px;background:linear-gradient(150deg,#c9c2b6,#7b6b58 50%,#2e3a55)}
  .reasons{left:260px;top:430px;width:300px;height:270px;background:var(--grey-mid);padding:34px 24px 0 26px;color:var(--white)}
  .reasons__title{font-weight:700;font-size:18px;line-height:1.2;padding-bottom:10px;border-bottom:2px solid var(--green);margin-bottom:10px}
  .reason{display:flex;gap:8px;font-size:10px;font-weight:500;line-height:1.35;margin-bottom:10px}
  .reason i{flex:0 0 12px;height:12px;border-radius:50%;background:var(--green);display:flex;align-items:center;justify-content:center;margin-top:1px}
  .back-footer{left:0;top:700px;width:560px;height:92px;background:var(--green);color:var(--white);font-weight:600;font-size:11px;display:flex;gap:34px;padding:20px 0 0 110px;line-height:1.6}
  .contact{display:flex;align-items:center;gap:6px}
  .contact--indent{padding-left:15px}
</style>
</head>
<body>
<div class="canvas">

  <section class="page page--front">
    <div class="abs hero" role="img" aria-label="Foto: Sicherheitsmitarbeiter im Einsatz, dunkel getönt"></div>
    <div class="abs top-rule"></div>
    <svg class="abs logo-tab" viewBox="0 0 320 88" aria-hidden="true"><polygon points="0,0 320,0 300,88 20,88" fill="#fff"/></svg>
    <div class="abs brand"><span class="brand__dot"></span>WACHKERN</div>
    <div class="abs brand-sub">SICHERHEITSTECHNIK</div>

    <h1 class="abs headline">
      <span class="headline__white">SCHÜTZEN SIE, WAS IHNEN</span>
      <span class="headline__green">AM WICHTIGSTEN IST!</span>
    </h1>
    <p class="abs tagline">Ihr Zuhause <b>•</b> Ihre Familie <b>•</b> Ihre Sicherheit.</p>

    <div class="abs thumbs">
      <div class="thumb thumb--touch" role="img" aria-label="Foto: Hand berührt digitales Schutzsymbol"></div>
      <div class="thumb thumb--cam" role="img" aria-label="Foto: Kuppel-Überwachungskamera an der Decke"></div>
      <div class="thumb thumb--phone" role="img" aria-label="Foto: Smartphone mit Smart-Home-Symbolen"></div>
    </div>
    <div class="abs question">Sind Sie wirklich sicher?</div>
    <p class="abs intro">Einbrüche, Vandalismus und Brände können unerwartet passieren. Schützen Sie Ihr Zuhause und gewinnen Sie ein gutes Gefühl von Sicherheit zurück.</p>

    <div class="abs guard-photo" role="img" aria-label="Foto: Sicherheitsmann von hinten im dunklen Shirt mit Aufschrift SICHERHEIT"></div>

    <div class="abs offer">
      <h2 class="offer__title">Entdecken Sie<br>modernste Lösungen für:</h2>
      <div class="offer__item">
        <div class="tick"><span><svg width="14" height="14" viewBox="0 0 14 14"><path d="M2 7l3.5 3.5L12 3.5" fill="none" stroke="#fff" stroke-width="2.4"/></svg></span></div>
        <div><div class="offer__name">Alarmanlagen</div><div class="offer__text">Effektiver Schutz vor Einbrüchen</div></div>
      </div>
      <div class="offer__item">
        <div class="tick"><span><svg width="14" height="14" viewBox="0 0 14 14"><path d="M2 7l3.5 3.5L12 3.5" fill="none" stroke="#fff" stroke-width="2.4"/></svg></span></div>
        <div><div class="offer__name">Kamerasysteme</div><div class="offer__text">Alles im Blick, jederzeit</div></div>
      </div>
      <div class="offer__item">
        <div class="tick"><span><svg width="14" height="14" viewBox="0 0 14 14"><path d="M2 7l3.5 3.5L12 3.5" fill="none" stroke="#fff" stroke-width="2.4"/></svg></span></div>
        <div><div class="offer__name">Brandmeldeanlagen</div><div class="offer__text">Frühzeitige Warnung rettet Leben</div></div>
      </div>
    </div>

    <div class="abs front-footer">Jetzt informieren und beruhigt in die Zukunft blicken!</div>
  </section>

  <section class="page page--back">
    <div class="abs fleet-photo" role="img" aria-label="Foto: Reihe weißer Firmentransporter mit grünem Streifen auf einem Parkplatz"></div>
    <div class="abs brand brand--small"><span class="brand__dot"></span>WACHKERN</div>
    <div class="abs brand-sub brand-sub--small">SICHERHEITSTECHNIK</div>

    <div class="abs dark-band"></div>
    <div class="abs benefits">
      <div class="benefit">
        <div class="ring"><span><svg width="24" height="26" viewBox="0 0 24 26"><path d="M12 2l9 3v7c0 6-4 10-9 12-5-2-9-6-9-12V5z" fill="none" stroke="#fff" stroke-width="2"/><path d="M8 13l3 3 5-6" fill="none" stroke="#fff" stroke-width="2"/></svg></span></div>
        <div><div class="benefit__title">Einbruchschutz:</div><div class="benefit__text">Jährlich werden tausende Haushalte Opfer von Einbrüchen. Ein professionelles Sicherheitssystem senkt das Risiko drastisch.</div></div>
      </div>
      <div class="benefit">
        <div class="ring"><span><svg width="26" height="22" viewBox="0 0 26 22"><path d="M2 11c3-5 7-7 11-7s8 2 11 7c-3 5-7 7-11 7S5 16 2 11z" fill="none" stroke="#fff" stroke-width="2"/><circle cx="13" cy="11" r="4" fill="#fff"/></svg></span></div>
        <div><div class="benefit__title">Überwachung:</div><div class="benefit__text">Modernste Kamerasysteme bieten Ihnen ein Auge vor Ort – auch, wenn Sie unterwegs sind.</div></div>
      </div>
      <div class="benefit">
        <div class="ring"><span><svg width="24" height="24" viewBox="0 0 24 24"><rect x="3" y="3" width="18" height="8" rx="2" fill="#fff"/><path d="M7 15c-1 2 1 3 0 5M12 15c-1 2 1 3 0 5M17 15c-1 2 1 3 0 5" fill="none" stroke="#fff" stroke-width="1.6"/></svg></span></div>
        <div><div class="benefit__title">Frühzeitige Brandmeldung:</div><div class="benefit__text">Brände sind unberechenbar. Eine schnelle Warnung schützt Leben und Eigentum.</div></div>
      </div>
    </div>
    <div class="abs why-tag">Warum Sie investieren sollten:</div>

    <div class="abs bags-photo" role="img" aria-label="Foto: Hand hält mehrere Einkaufstüten"></div>
    <div class="abs reasons">
      <h2 class="reasons__title">Warum Sie<br>investieren sollten:</h2>
      <div class="reason"><i><svg width="8" height="8" viewBox="0 0 8 8"><path d="M1 4l2 2 4-4" fill="none" stroke="#fff" stroke-width="1.4"/></svg></i>Rund-um-die-Uhr-Sicherheit</div>
      <div class="reason"><i><svg width="8" height="8" viewBox="0 0 8 8"><path d="M1 4l2 2 4-4" fill="none" stroke="#fff" stroke-width="1.4"/></svg></i>Einfache Bedienung und<br>modernste Technologie</div>
      <div class="reason"><i><svg width="8" height="8" viewBox="0 0 8 8"><path d="M1 4l2 2 4-4" fill="none" stroke="#fff" stroke-width="1.4"/></svg></i>Langfristige Investition in<br>Ihre Lebensqualität</div>
    </div>

    <footer class="abs back-footer">
      <div>
        <div class="contact"><svg width="10" height="10" viewBox="0 0 10 10"><circle cx="5" cy="5" r="4" fill="none" stroke="#fff" stroke-width="1.5"/></svg>brelling-schutz.de</div>
        <div class="contact"><svg width="10" height="10" viewBox="0 0 10 10"><path d="M2 1l2 2-1 1.5c.8 1.5 1.5 2.2 3 3L7.5 6l2 2-1.5 1.5C4.5 9 1 5.5.5 2z" fill="#fff"/></svg>034100/482913</div>
        <div class="contact"><svg width="10" height="10" viewBox="0 0 10 10"><rect x="1" y="1" width="8" height="8" rx="2" fill="none" stroke="#fff" stroke-width="1.3"/></svg>brelling_sdt</div>
      </div>
      <div>
        <div class="contact"><svg width="9" height="11" viewBox="0 0 9 11"><path d="M4.5 10.5S.5 6.5.5 4a4 4 0 018 0c0 2.5-4 6.5-4 6.5z" fill="none" stroke="#fff" stroke-width="1.3"/><circle cx="4.5" cy="4" r="1.3" fill="#fff"/></svg>Schutz, Ermittlung und Technik GmbH</div>
        <div class="contact--indent">Lindenweg 12</div>
        <div class="contact--indent">04100 Musterstadt</div>
      </div>
    </footer>
  </section>

</div>
</body>
</html>
```